Moonvale Jewellery Limited - designer pearl and silver jewellery

Designer silver jewellery with a twist that 20% of the net profit will be donated to a charity in India to help abused children

The products are designed to make the wearer not only feel good about how good the jewellery looks but to know they are also helping others less fortunate

All the Jewellery is designed by myself Margaret Doyle and made in 925 Hallmarked sterling silver . The hallmarking is carried out by the Corrick Assay office

This is my first website and will need to be suitable for e-commerce

Target Market(s)

Stylish women with a love of simple and elegant design , not high fashion by timeless simplicity

Number of Pages Required

5+ page

Font styles to use
Sans Serif

Colors
e666a6

Requirements
Must have
• Reference to Sterling silver
• The Pantone ref for my logo background now is white out of 2063
Nice to have
• Fresh and contemporary - Aimed at 25-55 market
• The same consumer would
• Like this product as likes Velmira, Kester Dunne but will also appreciate the fact this product is about helping others as well
• The Jewellery is about clean simple lines , elegance , hand made and styled to be timeless
• The products are designed to be casual and elegant and all feature either natural freshwater pearls or semi precious gemstones
• I also would like a page that customers can arrange to book talks about the design and production of the product . I give these talks generally tomladies groups and explain the manufacturing process and what the charity I’m doing supports

```html
<!DOCTYPE html>
<html lang="en">
<head>
<meta charset="utf-8">
<title>Moonvale Jewellery Limited</title>
<link rel="stylesheet" href="https://fonts.googleapis.com/css2?family=Arimo:wght@400;700&family=Gelasio:ital,wght@0,400;1,400&display=swap">
<style>
  :root {
    --pink: #e666a6;
    --teal: #00b3b3;
    --purple: #b07cf5;
    --paper: #f4f4f4;
    --ghost-card: #eef3f7;
    --orange: #ff6633;
    --ink: #555555;
    --body-ink: #4a4a4a;
    --muted: #a9a9a9;
    --icon-blue: #4a90d9;
    --white: #ffffff;
    --rule: #8a8a8a;
  }
  * { margin: 0; padding: 0; box-sizing: border-box; }
  html, body { width: 1200px; height: 2350px; overflow: hidden; }
  body { position: relative; background: var(--purple); font-family: "Arimo", Arial, sans-serif; }
  .abs { position: absolute; }
  .serif { font-family: "Gelasio", Georgia, serif; }

  /* Header */
  .site-header { left: 0; top: 0; width: 1200px; height: 107px; background: var(--pink); border-bottom: 1px solid var(--rule); }
  .main-nav a { position: absolute; top: 42px; color: var(--white); font-size: 13px; font-weight: 700; text-decoration: none; letter-spacing: 0.2px; }

  /* Intro */
  .intro { left: 0; top: 107px; width: 1200px; height: 684px; background: var(--paper); border: 1px solid #9a9a9a; }
  .intro-title { left: 0; top: 52px; width: 1200px; text-align: center; font-size: 37px; line-height: 47px; color: var(--ink); font-weight: 400; }
  .intro-copy { top: 162px; width: 300px; font-size: 12.5px; line-height: 22px; color: var(--body-ink); }
  .ghost-card { background: var(--ghost-card); }
  .feature-card { background: var(--pink); }
  .avatar { border-radius: 50%; background: var(--white); display: flex; align-items: center; justify-content: center; }
  .card-name { width: 100%; text-align: center; font-weight: 700; }
  .card-quote { width: 100%; text-align: center; font-style: italic; }
  .read-more { color: var(--white); font-size: 11px; }
  .book-talk { left: 78px; top: 598px; width: 196px; height: 55px; background: var(--orange); color: var(--white); font-style: italic; font-size: 18px; display: flex; align-items: center; justify-content: center; }

  .pink-band { left: 0; top: 791px; width: 1200px; height: 8px; background: var(--pink); }

  /* Explore */
  .explore { left: 0; top: 799px; width: 1200px; height: 777px; background: var(--teal); border: 1px solid #4a6f6f; }
  .explore-title { left: 0; top: 100px; width: 1200px; text-align: center; color: var(--white); font-size: 38px; font-weight: 400; }
  .category { top: 223px; width: 238px; height: 318px; }
  .category-image { left: 0; top: 0; width: 238px; height: 194px; background: var(--white); border-radius: 119px / 97px; display: flex; align-items: center; justify-content: center; }
  .product-shot { width: 140px; height: 120px; border-radius: 50%; }
  .category-label { left: 0; top: 189px; width: 238px; height: 129px; background: var(--pink); border-radius: 64px; display: flex; align-items: center; justify-content: center; color: var(--white); font-size: 30px; }
  .explore-copy { left: 340px; top: 620px; width: 520px; text-align: center; color: var(--white); font-size: 12.5px; line-height: 22px; }

  /* Team */
  .team { left: 0; top: 1577px; width: 1200px; height: 773px; background: var(--purple); border-top: 2px solid #5a3f7a; }
  .team-title { left: 177px; top: 232px; color: var(--white); font-size: 46px; font-weight: 400; }
  .team-copy { left: 177px; top: 318px; width: 420px; color: var(--white); font-size: 12.5px; line-height: 22px; }
  .team-tagline { left: 177px; top: 469px; color: var(--white); font-size: 12.5px; font-weight: 700; }
  .team-photo { left: 671px; top: 211px; width: 278px; height: 278px; border-radius: 50%; background: radial-gradient(circle at 50% 40%, #d9a98a 0%, #b77a5c 45%, #b52a22 80%, #8a2a20 100%); }
  .slider-dots { left: 790px; top: 535px; display: flex; gap: 9px; }
  .slider-dots span { width: 5px; height: 5px; border-radius: 50%; background: #e6dcf7; }
  .slider-dots span.active { background: var(--pink); }
</style>
</head>
<body>

<header class="site-header abs">
  <nav class="main-nav">
    <a style="left:713px">SHOP</a>
    <a style="left:785px">AUTHORS</a>
    <a style="left:879px">EXPLORE</a>
    <a style="left:971px">BLOG</a>
    <a style="left:1044px">CONTACT</a>
  </nav>
</header>

<section class="intro abs">
  <h1 class="intro-title abs serif">All the Jewellery is designed by myself<br>Margaret Doyle</h1>
  <p class="intro-copy abs" style="left:279px">Lorem ipsum dolor sit amet, consectetur adipisifwcing elit, sed do eiusmod tempor incididunt ut labore et dolore roipi magna aliqua. Ut enim ad minim veeniam, quis nostruklad</p>
  <p class="intro-copy abs" style="left:625px">Culpa qui officia deserunt mollit anim id est laborum. Sed ut perspiciatis unde omnis iste natus error sit voluptartem accusantium doloremque laudantium, totam rem aperiam, eaque ipsa quae</p>

  <!-- Testimonial cards -->
  <div class="ghost-card abs" style="left:279px; top:399px; width:171px; height:207px;">
    <div class="avatar abs" style="left:67px; top:22px; width:36px; height:36px;">
      <svg width="14" height="14" viewBox="0 0 16 16"><circle cx="8" cy="5" r="3.5" fill="#4a90d9"/><path d="M1.5 15c0-4 3-6 6.5-6s6.5 2 6.5 6z" fill="#4a90d9"/></svg>
    </div>
    <div class="card-name abs" style="top:66px; font-size:8px; color:var(--icon-blue); font-weight:400;">Name Surname</div>
    <div class="card-quote abs serif" style="top:90px; font-size:18px; line-height:28px; color:var(--muted);">Excepteur sint<br>occaecat</div>
  </div>

  <div class="ghost-card abs" style="left:754px; top:385px; width:167px; height:221px;">
    <div class="avatar abs" style="left:66px; top:27px; width:36px; height:36px;">
      <svg width="14" height="14" viewBox="0 0 16 16"><circle cx="8" cy="5" r="3.5" fill="#4a90d9"/><path d="M1.5 15c0-4 3-6 6.5-6s6.5 2 6.5 6z" fill="#4a90d9"/></svg>
    </div>
    <div class="card-name abs" style="top:76px; font-size:8px; color:var(--icon-blue); font-weight:400;">Name Surname</div>
    <div class="card-quote abs serif" style="top:96px; font-size:18px; line-height:28px; color:var(--muted);">Excepteur sint<br>occaecat</div>
  </div>

  <div class="feature-card abs" style="left:453px; top:296px; width:296px; height:329px;">
    <div class="avatar abs" style="left:115px; top:33px; width:66px; height:66px;">
      <svg width="20" height="20" viewBox="0 0 16 16"><circle cx="8" cy="5" r="3.5" fill="#4a90d9"/><path d="M1.5 15c0-4 3-6 6.5-6s6.5 2 6.5 6z" fill="#4a90d9"/></svg>
    </div>
    <div class="card-name abs" style="top:114px; font-size:11px; color:var(--white);">Name Surname</div>
    <div class="card-quote abs serif" style="top:144px; font-size:19px; line-height:28px; color:var(--white);">Excepteur sint occaecat<br>cupidatat non proident,<br>sunt in culpa qui officia</div>
    <div class="read-more abs" style="left:185px; top:290px;">Read More</div>
    <svg class="abs" style="left:258px; top:288px;" width="18" height="16" viewBox="0 0 18 16"><path d="M2 8h13M9 2l6 6-6 6" fill="none" stroke="#ffffff" stroke-width="2" stroke-linecap="round" stroke-linejoin="round"/></svg>
  </div>

  <div class="book-talk abs serif">Book Talk Now</div>
</section>

<div class="pink-band abs"></div>

<section class="explore abs">
  <h2 class="explore-title abs serif">Explore Now</h2>

  <div class="category abs" style="left:66px">
    <div class="category-image abs"><div class="product-shot" role="img" aria-label="Black pearl stud earrings" style="background:radial-gradient(circle, #5b5570 0%, #8f8aa0 40%, #ffffff 72%);"></div></div>
    <div class="category-label abs serif">Earring</div>
  </div>
  <div class="category abs" style="left:343px">
    <div class="category-image abs"><div class="product-shot" role="img" aria-label="Silver heart pendant filled with pearls" style="background:radial-gradient(circle, #ece6dc 0%, #c9c9cc 40%, #ffffff 72%);"></div></div>
    <div class="category-label abs serif">Bracelets</div>
  </div>
  <div class="category abs" style="left:621px">
    <div class="category-image abs"><div class="product-shot" role="img" aria-label="Silver ring with a single pearl" style="background:radial-gradient(circle, #e8ddd0 0%, #c8c8cc 40%, #ffffff 72%);"></div></div>
    <div class="category-label abs serif">Rings</div>
  </div>
  <div class="category abs" style="left:896px">
    <div class="category-image abs"><div class="product-shot" role="img" aria-label="Dark freshwater pearl bracelet" style="background:radial-gradient(circle, #ffffff 0%, #ffffff 30%, #6c6478 45%, #a49eb0 60%, #ffffff 74%);"></div></div>
    <div class="category-label abs serif">Necklaces</div>
  </div>

  <p class="explore-copy abs">Lorem ipsum dolor sit amet, consectetur adipisicing elit, sed do eiusmod tempor incididunt ut ero labore et dolore magna aliqua. Ut enim ad minim veniam, quis nostrud exercitation ullamco.</p>
</section>

<section class="team abs">
  <h2 class="team-title abs serif">Our Team.</h2>
  <p class="team-copy abs">Lorem ipsum dolor sit amet, consectetur adipisicing elit, sed do eiusmod tempor incididunt ut ero labore et dolore magna aliqua. Ut enim ad minim veniam, quis nostrud exercitation ullamco porili laboris nisi ut aliquip ex ea commodo consequat. Duis aute irure dolor in reprehenderit in uienply voluptate velit esse cillum dolore eu fugiat</p>
  <p class="team-tagline abs">LOREM IPSUM DOLOR AMET CONSECTETUER</p>
  <div class="team-photo abs" role="img" aria-label="Portrait of the jewellery designer"></div>
  <div class="slider-dots abs"><span class="active"></span><span></span><span></span><span></span></div>
</section>

</body>
</html>
```